A DL (210mm wide x 100mm deep) layered .psd prepared for print ready CMYK 300 dpi for gloss paper.

Target Market(s)

Business People & young professionals – middle – high income earners.

Requirements
Must have
• Heading:
TOP Brunch (big and bold)
Traders Owners Partners (smaller underneath)

Text:
Everything about the TOP Brunch is TOP. The TOP Brunches are aimed at Traders, Owners and Partners and are designed to be an environment for where people Thrive, Offer and Prosper, while learning Trade, Openness and Prudence.

These events will be held on Friday mornings at 7am on February 17, May 18, August 17 and November 16, 2012.

The Velvet Playhouse, 412 Marlow Lane, Newcastle.
For more information, Phone (02) 4813 5062 or email info@chapel365.example

Please include:
SFP Logo, Chapel365 Logo, & TOP Logo
Nice to have
• Open to blue colours refer to steadyfundplanning.example and Chapel365.example

- Open to graphics/illustrations/photos - Can also purchase images from PixVault.
Should not have
• Too Much Bright Red or Yellow (open to some but not like a Burgertown flyer)

```html
<!DOCTYPE html>
<html lang="en">
<head>
<meta charset="utf-8">
<title>TOP Brunch 2012</title>
<link rel="stylesheet" href="https://fonts.googleapis.com/css2?family=Archivo+Black&family=Open+Sans:wght@400;600;700&display=swap">
<style>
  :root {
    --sky-top: #2c5a8e;
    --sky-mid: #86abd0;
    --sky-pale: #dfe8ef;
    --horizon: #c9a27a;
    --sunset: #c9792f;
    --sunset-deep: #5e341f;
    --navy: #13294a;
    --ink: #111820;
    --white: #ffffff;
    --cyan: #2fb8ec;
    --gold: #f6c21c;
    --logo-blue: #1f5aa8;
  }
  * { margin: 0; padding: 0; box-sizing: border-box; }
  html, body { width: 1200px; height: 569px; overflow: hidden; background: #fff; }
  .flyer {
    position: relative;
    width: 1200px;
    height: 569px;
    overflow: hidden;
    font-family: "Open Sans", sans-serif;
  }
  .sky-photo {
    position: absolute;
    inset: 0;
    background: linear-gradient(180deg, var(--sky-top) 0%, var(--sky-mid) 26%, var(--sky-pale) 46%, var(--horizon) 64%, var(--sunset) 80%, var(--sunset-deep) 100%);
  }
  .headline-top {
    position: absolute;
    left: 30px;
    top: -18px;
    font-family: "Archivo Black", sans-serif;
    font-size: 290px;
    line-height: 1;
    letter-spacing: -12px;
    transform: scaleY(1.3);
    transform-origin: left top;
    background: linear-gradient(180deg, rgba(30,70,125,0.9) 0%, rgba(150,185,215,0.85) 45%, rgba(245,248,250,0.95) 100%);
    -webkit-background-clip: text;
    background-clip: text;
    color: transparent;
    filter: drop-shadow(0 2px 3px rgba(0,0,0,0.35));
  }
  .tagline-bar {
    position: absolute;
    left: 40px;
    top: 329px;
    width: 603px;
    height: 33px;
    background: var(--navy);
    border: 1px solid rgba(255,255,255,0.5);
    color: var(--white);
    font-size: 20px;
    font-weight: 600;
    letter-spacing: 2.5px;
    display: flex;
    align-items: center;
    justify-content: center;
    gap: 14px;
  }
  .tagline-bar .divider { opacity: 0.8; font-weight: 400; }
  .headline-event {
    position: absolute;
    left: 32px;
    top: 364px;
    font-family: "Archivo Black", sans-serif;
    font-size: 112px;
    line-height: 1;
    letter-spacing: 6px;
    white-space: nowrap;
    background: linear-gradient(180deg, rgba(255,255,255,0.97) 0%, rgba(225,220,215,0.85) 60%, rgba(200,190,180,0.8) 100%);
    -webkit-background-clip: text;
    background-clip: text;
    color: transparent;
    filter: drop-shadow(0 2px 3px rgba(0,0,0,0.4));
  }
  .partners {
    position: absolute;
    left: 673px;
    top: 48px;
    width: 494px;
    height: 40px;
    display: flex;
    align-items: center;
    justify-content: space-between;
    font-weight: 700;
    font-size: 26px;
    color: var(--logo-blue);
  }
  .partner { display: flex; align-items: center; gap: 8px; }
  .partner-dot { width: 12px; height: 12px; border-radius: 50%; background: var(--logo-blue); }
  .schedule {
    position: absolute;
    left: 690px;
    top: 114px;
    width: 530px;
    text-align: center;
    color: var(--ink);
    font-size: 29px;
    line-height: 1.2;
  }
  .schedule strong { font-weight: 700; }
  .schedule .dates { font-weight: 700; font-size: 35px; line-height: 1.15; }
  .intro {
    position: absolute;
    left: 700px;
    top: 308px;
    width: 490px;
    color: var(--ink);
    font-size: 12px;
    line-height: 1.3;
    text-align: center;
  }
  .footer {
    position: absolute;
    top: 520px;
    font-size: 16px;
    font-weight: 700;
    white-space: nowrap;
  }
  .venue { left: 37px; color: var(--cyan); text-transform: uppercase; }
  .contact { left: 587px; color: var(--gold); font-weight: 600; }
</style>
</head>
<body>
<main class="flyer">
  <div class="sky-photo" role="img" aria-label="Photograph of a sky at sunrise, blue clouds above and a golden horizon below"></div>

  <h1 class="headline-top">TOP</h1>
  <p class="tagline-bar"><span>Traders</span><span class="divider">|</span><span>Owners</span><span class="divider">|</span><span>Partners</span></p>
  <p class="headline-event">BRUNCH 2012</p>

  <div class="partners">
    <span class="partner"><span class="partner-dot"></span>SFP</span>
    <span class="partner">TOP</span>
    <span class="partner">Chapel365</span>
  </div>

  <p class="schedule">
    Events will be held<br>
    on Friday mornings at <strong>7am</strong>,<br>
    starting on<br>
    <span class="dates">Feb 17, May 18,<br>Aug 17 and Nov 16</span>
  </p>

  <p class="intro">Everything about the TOP Brunch is TOP. The TOP Brunches are aimed at Traders, Owners and Partners and are designed to be an environment for where people Thrive, Offer and Prosper, while learning Trade, Openness and Prudence.</p>

  <p class="footer venue">The Velvet Playhouse, 412 Marlow Lane, Newcastle</p>
  <p class="footer contact">For more info, call (02) 4813 5062 or email us at info@chapel365.example</p>
</main>
</body>
</html>
```